Business Card for Financial Asset Management Company

Now we are launching a new company based in Tokyo.
The company information is below;

Company Name: Talvane Management

Operations: Financial assets management, Proposing forming portfolio of assets, Consulting service, and advising to enhance your company's financial health

Corporate Colour: Japan Blue or Navy like below
http://staffpages.qorvenly.edu/mtavis/images/Slate/Teal-Slate-217.jpg

It's dark and deep, and will get to fit to our clients as our relationships last longer and longer.

Our images for this colour are "Japanese style" and "pride in our craftmanship" , and also "gentle".

Corporate Key Image: an order taker who is sincere, polite, but courageous

We don't have our logo yet so please feel free to put any symbol on your design.

Please do not hesitate about asking any questions.
Thank you :-)

Reason: We are still discussin on final decision. Thank you for your understanding.

```html
<!DOCTYPE html>
<html lang="en">
<head>
<meta charset="utf-8">
<title>Talvane Management – Business Card</title>
<link rel="stylesheet" href="https://fonts.googleapis.com/css2?family=Open+Sans:wght@400;600;700&display=swap">
<style>
  :root {
    --page-bg: #d3d3d5;
    --navy-deep: #14133a;
    --navy: #2b2a72;
    --navy-light: #3a3890;
    --ink: #1c1b4f;
    --text-dark: #1a1a1a;
    --white: #ffffff;
    --kanji-grey: #dcdcdc;
  }
  * { box-sizing: border-box; margin: 0; padding: 0; }
  html, body {
    width: 883px;
    height: 1200px;
    overflow: hidden;
    background: var(--page-bg);
    font-family: "Open Sans", Arial, sans-serif;
  }
  .card {
    position: absolute;
    left: 91px;
    width: 700px;
    height: 392px;
    overflow: hidden;
    box-shadow: 0 6px 18px rgba(0,0,0,0.18);
  }
  .card-front {
    top: 188px;
    background: linear-gradient(160deg, var(--navy-light) 0%, var(--navy) 40%, var(--navy-deep) 100%);
  }
  .card-back {
    top: 620px;
    background: var(--white);
  }
  .front-waves { position: absolute; inset: 0; }

  .brand-circle {
    position: absolute;
    border-radius: 50%;
  }
  .card-front .brand-circle {
    left: 86px; top: 152px; width: 80px; height: 80px;
    border: 5px solid var(--white);
  }
  .card-back .brand-circle {
    left: 316px; top: 43px; width: 58px; height: 58px;
    border: 4px solid var(--ink);
  }
  .brand-divider { position: absolute; width: 2px; }
  .card-front .brand-divider { left: 285px; top: 122px; height: 144px; background: rgba(255,255,255,0.85); }
  .card-back .brand-divider { left: 447px; top: 18px; height: 104px; background: var(--ink); }

  .brand-name { position: absolute; font-weight: 700; line-height: 1.05; }
  .card-front .brand-name { left: 310px; top: 142px; font-size: 42px; color: var(--white); }
  .card-back .brand-name { left: 465px; top: 39px; font-size: 30px; color: var(--ink); }

  .name-band {
    position: absolute;
    left: 0; top: 40px;
    width: 291px; height: 68px;
    background: var(--navy);
    color: var(--white);
    padding: 6px 0 0 45px;
  }
  .person-name { font-size: 25px; font-weight: 400; line-height: 1.2; }
  .person-title { font-size: 18px; line-height: 1.1; }

  .address {
    position: absolute;
    left: 45px; top: 158px;
    font-size: 19px; line-height: 24px;
    color: var(--text-dark);
  }
  .contact-list {
    position: absolute;
    left: 43px; top: 248px;
    list-style: none;
    font-size: 19px; line-height: 21px;
    color: var(--text-dark);
  }
  .contact-list li { display: flex; align-items: center; }
  .contact-icon { width: 22px; height: 16px; margin-right: 10px; color: var(--navy); flex: none; }
  .contact-fx { font-size: 14px; color: var(--navy); width: 22px; margin-right: 10px; }

  .kanji-mark {
    position: absolute;
    left: 291px; top: 140px;
    width: 377px; height: 225px;
    background: linear-gradient(90deg, var(--kanji-grey), #e6e6e6);
    opacity: 0.8;
  }
</style>
</head>
<body>

<section class="card card-front">
  <svg class="front-waves" viewBox="0 0 700 392" preserveAspectRatio="none" aria-hidden="true">
    <path d="M250 0 C420 120 560 200 700 210 L700 0 Z" fill="rgba(255,255,255,0.05)"/>
    <path d="M380 392 C460 250 560 170 700 140 L700 392 Z" fill="rgba(255,255,255,0.04)"/>
    <path d="M0 392 C150 300 300 300 460 392 Z" fill="rgba(0,0,0,0.18)"/>
  </svg>
  <div class="brand-circle"></div>
  <div class="brand-divider"></div>
  <div class="brand-name">Talvane<br>Management</div>
</section>

<section class="card card-back">
  <div class="name-band">
    <p class="person-name">Mariko Sanada</p>
    <p class="person-title">title here</p>
  </div>

  <div class="brand-circle"></div>
  <div class="brand-divider"></div>
  <div class="brand-name">Talvane<br>Management</div>

  <p class="address">Your address can put here<br>Your address can put here</p>

  <ul class="contact-list">
    <li>
      <svg class="contact-icon" viewBox="0 0 22 16" aria-hidden="true"><path d="M3 5 Q11 0 19 5 L17 8 L14 6 L8 6 L5 8 Z M6 9 H16 L17 15 H5 Z" fill="currentColor"/></svg>
      0123 456 789
    </li>
    <li>
      <svg class="contact-icon" viewBox="0 0 22 16" aria-hidden="true"><rect x="7" y="1" width="8" height="14" rx="1" fill="none" stroke="currentColor" stroke-width="1.5"/></svg>
      0123 456 789
    </li>
    <li><span class="contact-fx">Fx</span>0123 456 789</li>
    <li>
      <svg class="contact-icon" viewBox="0 0 22 16" aria-hidden="true"><rect x="4" y="3" width="14" height="10" fill="currentColor"/><path d="M4 3 L11 9 L18 3" fill="none" stroke="#fff" stroke-width="1.2"/></svg>
      youremail@mail.com
    </li>
  </ul>

  <div class="kanji-mark" role="img" aria-label="Large faint hand-brushed kanji for Tokyo"></div>
</section>

</body>
</html>
```